I am a business consultant/coach and I am branding myself 'The Zero Fee Venture Mentor'. My business name is Bright Harbor Advisory.I want an oversized postcard designed for lead generation. It will be sent through the post so will require area for an address and stamp The details that I want on the card are attached plus a photo of myself. Also I have attached a copy of my business card so that you are able to see the style and colors I use. I would like the main headline to be bold red, or bold red background Hope this is enough info.
Target Market(s)
Owners/managers of medium sized businesses
Industry/Entity Type
Business Consultant
Requirements
Must have
- The cards I want to be noticed and professional in appearance, they will be use dfor lead generation and sent through the postal service
Nice to have
- The colors that I use on my business cards are green, grey and white. I want the main headline to be in red or red backgroun dso that it stands out
Should not have
- The words that I have used are basically off my landing page for consistency

```html
<!DOCTYPE html>
<html lang="en">
<head>
<meta charset="utf-8">
<title>Bright Harbor Advisory – Lead Generation Postcard</title>
<link href="https://fonts.googleapis.com/css2?family=Bebas+Neue&family=Lato:ital,wght@0,400;0,700;0,900;1,400;1,700;1,900&display=swap" rel="stylesheet">
<style>
  :root{
    --red:#e3222c;
    --red-dark:#c81a23;
    --green:#9bc93b;
    --green-light:#b5d94f;
    --ink:#2b2b2b;
    --grey-mid:#9a9a9a;
    --charcoal:#3a3a3a;
    --white:#ffffff;
    --page:#eeeeee;
    --rule:#b9b9b9;
  }
  *{box-sizing:border-box;margin:0;padding:0}
  html,body{width:900px;height:1200px;overflow:hidden}
  body{background:var(--page);font-family:"Lato",Arial,sans-serif;color:var(--ink);position:relative}

  .card{position:absolute;left:97px;width:706px;background:var(--white);box-shadow:0 3px 10px rgba(0,0,0,.25);overflow:hidden}
  .card--front{top:38px;height:548px}
  .card--back{top:622px;height:546px}

  /* FRONT */
  .brand{position:absolute;left:0;top:0;width:220px;height:140px;display:flex;align-items:center;justify-content:center;gap:8px}
  .brand__mark{width:14px;height:14px;background:var(--green)}
  .brand__name{font-family:"Lato",sans-serif;font-weight:900;font-size:25px;color:var(--charcoal);letter-spacing:-.3px}

  .headline{position:absolute;left:220px;top:0;right:0;height:140px;background:linear-gradient(180deg,#ee3a42,var(--red) 50%,var(--red-dark));padding:28px 0 0 20px;font-family:"Bebas Neue",sans-serif;font-weight:400;font-size:46px;line-height:44px;text-transform:uppercase;white-space:nowrap}
  .headline__line1{color:var(--white)}
  .headline__line2{color:var(--ink)}
  .headline-shadow{position:absolute;left:220px;top:140px;right:0;height:6px;background:linear-gradient(var(--grey-mid),transparent)}

  .offer-band{position:absolute;left:0;top:146px;width:706px;height:62px;background:linear-gradient(180deg,var(--green-light),var(--green));padding:17px 0 0 20px;font-family:"Bebas Neue",sans-serif;font-size:31px;line-height:30px;color:var(--ink);text-transform:uppercase;white-space:nowrap}

  .portrait{position:absolute;background:radial-gradient(ellipse at 50% 42%,#e9b6a0 0 26%,#c98f77 38%,#8a8a8a 55%,#f3f3f3 74%)}
  .portrait--front{left:482px;top:140px;width:218px;height:268px}
  .portrait--back{left:242px;top:300px;width:94px;height:149px}

  .pitch{position:absolute;left:20px;top:230px;width:450px;font-style:italic;font-weight:700;font-size:18.5px;line-height:24px;color:var(--ink);white-space:nowrap}
  .proof{position:absolute;left:0;top:327px;width:465px;height:48px;border-radius:0 24px 24px 0;background:linear-gradient(180deg,#fafafa,#cfcfcf);box-shadow:0 2px 4px rgba(0,0,0,.3);padding:10px 0 0 18px;font-style:italic;font-weight:700;font-size:24px;line-height:28px;color:var(--red);white-space:nowrap}

  .cta-band{position:absolute;left:0;top:408px;width:706px;height:96px;background:linear-gradient(180deg,var(--green-light),var(--green))}
  .cta{position:absolute;left:26px;top:430px;font-family:"Bebas Neue",sans-serif;color:var(--white);font-size:34px;line-height:48px;white-space:nowrap}
  .cta__number{color:var(--ink);font-size:46px;margin-left:4px}
  .signature{position:absolute;left:384px;top:408px;width:322px;height:96px;background:linear-gradient(180deg,#f2f2f2,#c9c9c9);border-radius:34px 0 0 0;padding:17px 0 0 12px;font-size:15px;line-height:21px;font-weight:700;text-align:center;white-space:nowrap}
  .signature__name{color:var(--ink)}
  .signature__name strong{font-weight:900}
  .signature__org{color:var(--red)}
  .base-bar{position:absolute;left:0;top:504px;width:706px;height:44px;background:linear-gradient(180deg,#5a5a5a,#2a2a2a)}

  /* BACK */
  .reason{position:absolute;left:0;top:0;width:331px;height:114px;background:var(--red);padding:8px 16px;color:var(--white)}
  .section-title{font-family:"Bebas Neue",sans-serif;font-weight:400;font-size:21px;text-transform:uppercase;line-height:22px}
  .section-text{font-style:italic;font-weight:700;font-size:11.5px;line-height:16px}
  .problem{position:absolute;left:0;top:119px;width:331px;height:89px;background:var(--green);padding:6px 16px;color:var(--ink)}
  .solution{position:absolute;left:16px;top:218px;width:305px;font-size:12.5px;line-height:16.5px;color:var(--ink)}
  .promise{position:absolute;left:0;top:312px;width:331px;height:137px;background:linear-gradient(180deg,#4a4a4a,#2d2d2d)}
  .promise__title{position:absolute;left:18px;top:4px;font-family:"Lato",sans-serif;font-weight:700;font-size:14px;line-height:16px;color:var(--green);text-transform:uppercase}
  .promise__text{position:absolute;left:18px;top:22px;width:215px;font-style:italic;font-weight:700;font-size:9px;line-height:12.5px;color:var(--white)}
  .more-info{position:absolute;left:0;top:380px;width:242px;height:17px;background:var(--green);padding:3px 18px;font-size:9px;line-height:11px;font-weight:700;color:var(--ink);white-space:nowrap}
  .contacts{position:absolute;left:18px;top:401px;list-style:none;font-size:9px;line-height:14px;color:var(--white);white-space:nowrap}
  .contacts li{display:flex;align-items:center;gap:6px}
  .contacts svg{width:8px;height:8px;flex:none}
  .divider{position:absolute;left:331px;top:0;width:16px;height:449px;background:linear-gradient(90deg,var(--charcoal) 0 6px,var(--green) 6px)}
  .stamp{position:absolute;left:544px;top:36px;width:127px;height:138px;background:#ececec}
  .address-line{position:absolute;left:393px;width:278px;height:1px;background:var(--rule)}
  .address-line--1{top:219px}
  .address-line--2{top:285px}
  .address-line--3{top:347px}
</style>
</head>
<body>

<section class="card card--front" aria-label="Postcard front">
  <div class="brand"><span class="brand__mark"></span><span class="brand__name">Bright Harbor</span></div>
  <h1 class="headline"><span class="headline__line1">Has your business achieved</span><br><span class="headline__line2">the outcomes you want?</span></h1>
  <div class="headline-shadow"></div>
  <div class="offer-band">It can and I’m prepared to show you how</div>
  <div class="portrait portrait--front" role="img" aria-label="Portrait photo of the consultant, smiling, white shirt"></div>
  <p class="pitch">If I told you that you can increase your profits,<br>give yourself more time, freedom and peace,<br>what would your answer be…?</p>
  <p class="proof">Research says you can and quickly</p>
  <div class="cta-band"></div>
  <p class="cta">Call me on <span class="cta__number">0412 555 018</span></p>
  <div class="signature">
    <div class="signature__name">My name is <strong>DANIEL WHITAKER</strong></div>
    <div class="signature__org">from Bright Harbor Advisory,<br>the ‘Zero Fee Venture Mentor’.</div>
  </div>
  <div class="base-bar"></div>
</section>

<section class="card card--back" aria-label="Postcard back">
  <div class="reason">
    <h2 class="section-title">Because</h2>
    <p class="section-text">Over 90 percent of small to medium sized business in Australia have a minimum of 12 per cent of their annual turnover tied up in ineffective and inefficient processes?</p>
  </div>
  <div class="problem">
    <h2 class="section-title">The problem is that</h2>
    <p class="section-text">Most business owners focus on their daily challenges unable to free themselves to consider where the ‘hidden profit’ may be locked up within their business.</p>
  </div>
  <p class="solution">I can change this by reviewing your cashflow, systems, staff capability, business culture and Risk. The end result will be more Peace of Mind to live your life that way you desire.</p>
  <div class="promise">
    <h3 class="promise__title">My promise:</h3>
    <p class="promise__text">If I cannot uncover at least 5 times my fee from potential profits hidden with your business after one interview then it is free.</p>
  </div>
  <p class="more-info">If you would like more information go to</p>
  <ul class="contacts">
    <li><svg viewBox="0 0 8 8"><circle cx="4" cy="4" r="3.4" fill="none" stroke="#9bc93b" stroke-width="1.2"/></svg>www.brightharbor.com.au/zerofee</li>
    <li><svg viewBox="0 0 8 8"><rect x="0.6" y="1.6" width="6.8" height="4.8" fill="none" stroke="#9bc93b" stroke-width="1.1"/><path d="M0.6 1.6 4 4.5 7.4 1.6" fill="none" stroke="#9bc93b" stroke-width="1"/></svg>email hello@brightharbor.com.au</li>
    <li><svg viewBox="0 0 8 8"><path d="M1.5 0.8 3 2.6 2.2 3.6a4 4 0 0 0 2.2 2.2l1-0.8 1.8 1.5-1 1.2C3 7.6 0.4 5 0.3 1.8z" fill="#9bc93b"/></svg>0412 555 018</li>
  </ul>
  <div class="portrait portrait--back" role="img" aria-label="Small portrait photo of the consultant"></div>
  <div class="divider"></div>
  <div class="stamp" aria-label="Stamp area"></div>
  <div class="address-line address-line--1"></div>
  <div class="address-line address-line--2"></div>
  <div class="address-line address-line--3"></div>
</section>

</body>
</html>
```